Taomeng business card -we import and distributed Chinese herbal medicine into Australia for prac...

We need a business card for our recently purchased and rebranded company. We are a small family run business - husband and wife team. Our logo is red and black, and we would like the card to be white, with an element of gold in the design (the first cloud in the attached png) which when printed we would like embossed in gold. Our website uses Chinese water colour paintings in the banners (www.taomeng.net.au) so a design that is in harmony with this would be ideal.
side one needs to include:

Target Market(s)

potential customers

Industry/Entity Type

Health And Wellness

Contact Information for Business Card

Side 1
logo,
Edmund Varsk Director
Practitioner Support and Education
0491 722 413
edmund@taomeng.net.au
218 Colbury St, Harlow Ridge, SA, 5291

side 2 needs to include:
logo
Priscilla Moult Director
Orders, Accounts and Despatch
0487 530 619
priscilla@taomeng.net.au

Font styles to use
Serif

Colors

Designer to choose colors to be used in the design.

Requirements
Must have
• black, red, gold colours
Nice to have
• we like the font papyrus (mac font)

```html
<!DOCTYPE html>
<html lang="en">
<head>
<meta charset="utf-8">
<title>Taomeng Business Cards</title>
<link rel="stylesheet" href="https://fonts.googleapis.com/css2?family=Lora:wght@400;500;700&display=swap">
<style>
  :root {
    --board: #5f5f5f;
    --card: #ffffff;
    --card-edge: #8a8a8a;
    --ink: #1e2340;
    --text: #111111;
    --seal-red: #de3a2c;
    --gold: #f2c45c;
    --wash-deep: #2f5479;
    --wash-mid: #7b9bbb;
    --wash-pale: #d9e3ee;
  }
  * { box-sizing: border-box; margin: 0; padding: 0; }
  html, body {
    width: 1036px;
    height: 1200px;
    overflow: hidden;
    background: var(--board);
  }
  .sheet {
    position: relative;
    width: 1036px;
    height: 1200px;
    font-family: "Lora", Georgia, serif;
  }
  .card {
    position: absolute;
    left: 35px;
    width: 968px;
    height: 554px;
    background: var(--card);
    border: 2px solid var(--card-edge);
    box-shadow: 4px 4px 6px rgba(0,0,0,0.35);
    overflow: hidden;
  }
  .card--front { top: 35px; }
  .card--back { top: 617px; }

  .brand {
    position: absolute;
    left: 74px;
    top: 88px;
    display: flex;
    align-items: center;
    gap: 26px;
  }
  .brand__seal {
    width: 71px;
    height: 152px;
    background: var(--seal-red);
    border-radius: 3px;
    flex: none;
  }
  .brand__name {
    font-weight: 500;
    font-size: 78px;
    line-height: 0.98;
    letter-spacing: 2px;
    color: var(--ink);
  }
  .brand__name span { display: block; }

  .divider {
    position: absolute;
    left: 440px;
    top: 50px;
    width: 3px;
    height: 236px;
    background: var(--gold);
  }

  .contact {
    position: absolute;
    left: 478px;
    top: 52px;
    width: 420px;
    text-align: center;
    color: var(--text);
    font-size: 21px;
    line-height: 42px;
  }
  .contact__name { font-weight: 700; }

  .cloud {
    position: absolute;
    left: 641px;
    top: 226px;
    width: 122px;
    height: 53px;
    border-radius: 30px 40px 18px 26px;
    background: var(--gold);
  }

  .landscape {
    position: absolute;
    left: 0;
    top: 270px;
    width: 968px;
    height: 222px;
    background:
      radial-gradient(ellipse 30% 55% at 24% 55%, rgba(47,84,121,0.75), transparent 70%),
      radial-gradient(ellipse 22% 45% at 62% 58%, rgba(47,84,121,0.7), transparent 70%),
      radial-gradient(ellipse 18% 40% at 88% 40%, rgba(47,84,121,0.55), transparent 70%),
      radial-gradient(ellipse 55% 60% at 50% 55%, var(--wash-mid), transparent 80%),
      linear-gradient(180deg, transparent 0%, var(--wash-pale) 35%, var(--wash-pale) 75%, transparent 100%);
  }

  .address {
    position: absolute;
    left: 0;
    top: 498px;
    width: 968px;
    text-align: center;
    font-weight: 700;
    font-size: 23px;
    color: var(--ink);
  }
</style>
</head>
<body>
<main class="sheet">

  <section class="card card--front">
    <div class="brand">
      <div class="brand__seal"></div>
      <div class="brand__name"><span>TAO</span><span>MENG</span></div>
    </div>
    <div class="divider"></div>
    <div class="contact">
      <p class="contact__name">Edmund Varsk Director</p>
      <p>Practitioner Support and Education</p>
      <p>0491 722 413</p>
      <p>edmund@taomeng.net.au</p>
    </div>
    <div class="cloud" role="img" aria-label="Gold auspicious cloud ornament, to be foil embossed"></div>
    <div class="landscape" role="img" aria-label="Chinese watercolour painting of misty blue mountains"></div>
    <p class="address">218 Colbury St, Harlow Ridge, SA, 5291</p>
  </section>

  <section class="card card--back">
    <div class="brand">
      <div class="brand__seal"></div>
      <div class="brand__name"><span>TAO</span><span>MENG</span></div>
    </div>
    <div class="divider"></div>
    <div class="contact">
      <p class="contact__name">Priscilla Moult Director</p>
      <p>Orders, Accounts and Despatch</p>
      <p>0487 530 619</p>
      <p>priscilla@taomeng.net.au</p>
    </div>
    <div class="cloud" role="img" aria-label="Gold auspicious cloud ornament, to be foil embossed"></div>
    <div class="landscape" role="img" aria-label="Chinese watercolour painting of misty blue mountains"></div>
    <p class="address">218 Colbury St, Harlow Ridge, SA, 5291</p>
  </section>

</main>
</body>
</html>
```